LumaVantix
stationery - business cards
LumaVantix -
Creative Brief
Professional
Carl MORVEDO
41 Pellin Lane, suite 218 San Mateo, California, 94402
cm@lumavantix.com
www.lumavantix.com
Free to be creative

```html
<!DOCTYPE html>
<html lang="en">
<head>
<meta charset="utf-8">
<title>LumaVantix Business Cards</title>
<link rel="stylesheet" href="https://fonts.googleapis.com/css2?family=Open+Sans:wght@400;600;700&display=swap">
<style>
  :root {
    --page-bg: #e9eaec;
    --card-dark: #161616;
    --card-dark-2: #2a2a2a;
    --card-light: #ffffff;
    --accent-blue: #1f6fc4;
    --accent-blue-light: #4a97e0;
    --text-dark: #3a3f47;
    --text-name: #24456e;
    --text-muted: #555b63;
    --shape-faint-light: #eef0f3;
    --shape-faint-dark: #232323;
  }
  html, body {
    margin: 0;
    padding: 0;
    width: 1200px;
    height: 901px;
    overflow: hidden;
    background: var(--page-bg);
    font-family: "Open Sans", Arial, sans-serif;
  }
  .canvas {
    position: relative;
    width: 1200px;
    height: 901px;
  }
  .card {
    position: absolute;
    top: 280px;
    width: 536px;
    height: 304px;
    border-radius: 18px;
    overflow: hidden;
    box-shadow: 0 6px 18px rgba(0,0,0,0.18);
  }
  .card-front {
    left: 41px;
    background: linear-gradient(180deg, var(--card-dark-2) 0%, var(--card-dark) 60%, #0c0c0c 100%);
  }
  .card-back {
    left: 604px;
    background: var(--card-light);
  }
  .card-art {
    position: absolute;
    inset: 0;
  }
  .brand {
    position: absolute;
    display: flex;
    align-items: center;
    gap: 10px;
    font-weight: 600;
    letter-spacing: 0.5px;
    white-space: nowrap;
  }
  .brand-mark { display: block; }
  .card-front .brand {
    right: 34px;
    top: 30px;
    font-size: 40px;
    color: #ffffff;
  }
  .card-front .brand-mark {
    width: 40px;
    height: 40px;
    background: #ffffff;
  }
  .card-back .brand {
    left: 44px;
    top: 42px;
    font-size: 30px;
    color: var(--text-dark);
  }
  .card-back .brand-mark {
    width: 30px;
    height: 30px;
    background: var(--accent-blue);
  }
  .web {
    position: absolute;
    display: flex;
    align-items: center;
    gap: 7px;
    font-size: 12px;
    white-space: nowrap;
  }
  .card-front .web {
    right: 30px;
    bottom: 32px;
    color: #d8d8d8;
  }
  .card-back .web {
    right: 28px;
    top: 248px;
    color: var(--text-muted);
  }
  .person-name {
    position: absolute;
    right: 44px;
    top: 52px;
    font-size: 22px;
    color: var(--text-name);
    display: flex;
    align-items: center;
    gap: 8px;
    white-space: nowrap;
  }
  .person-name .surname { font-weight: 700; }
  .person-name .name-tick {
    width: 10px;
    height: 14px;
    background: var(--accent-blue);
  }
  .contact {
    position: absolute;
    left: 30px;
    top: 196px;
    font-size: 12.5px;
    line-height: 20px;
    color: var(--text-dark);
    margin: 0;
    padding: 0;
    list-style: none;
    white-space: nowrap;
  }
  .contact li {
    display: flex;
    align-items: center;
    gap: 6px;
  }
  .icon { flex: none; }
</style>
</head>
<body>
<main class="canvas">

  <section class="card card-front" aria-label="Business card front">
    <svg class="card-art" width="536" height="304" viewBox="0 0 536 304" aria-hidden="true">
      <polygon points="250,60 340,150 250,240 160,150" fill="var(--shape-faint-dark)"/>
      <polygon points="360,40 460,140 360,240 260,140" fill="var(--shape-faint-dark)" opacity="0.7"/>
      <polygon points="0,82 26,82 74,142 26,202 0,202" fill="var(--accent-blue)"/>
      <polygon points="0,110 14,110 40,142 14,174 0,174" fill="var(--accent-blue-light)" opacity="0.6"/>
      <rect x="0" y="250" width="536" height="54" fill="#0a0a0a" opacity="0.6"/>
    </svg>
    <div class="brand"><span class="brand-mark"></span>LumaVantix</div>
    <div class="web">
      <svg class="icon" width="14" height="14" viewBox="0 0 14 14"><circle cx="7" cy="7" r="6" fill="none" stroke="#d8d8d8" stroke-width="1.4"/><path d="M1 7h12M7 1c3 3 3 9 0 12M7 1c-3 3-3 9 0 12" fill="none" stroke="#d8d8d8" stroke-width="1"/></svg>
      www.lumavantix.com
    </div>
  </section>

  <section class="card card-back" aria-label="Business card back">
    <svg class="card-art" width="536" height="304" viewBox="0 0 536 304" aria-hidden="true">
      <rect x="200" y="70" width="130" height="130" rx="18" transform="rotate(45 265 135)" fill="var(--shape-faint-light)"/>
      <polygon points="536,74 500,74 456,152 500,230 536,230" fill="var(--shape-faint-light)"/>
      <polygon points="536,96 518,96 488,152 518,208 536,208" fill="var(--accent-blue)"/>
    </svg>
    <div class="brand"><span class="brand-mark"></span>LumaVantix</div>
    <div class="person-name"><span>Carl <span class="surname">MORVEDO</span></span><span class="name-tick"></span></div>
    <ul class="contact">
      <li>
        <svg class="icon" width="12" height="12" viewBox="0 0 12 12"><path d="M6 1 1 5.5h1.6V11h2.8V8h1.2v3h2.8V5.5H11z" fill="var(--accent-blue)"/></svg>
        : 41 Pellin Lane, Suite
      </li>
      <li>218 Ferndale Springs California</li>
      <li>95871
        <svg class="icon" width="12" height="12" viewBox="0 0 12 12"><path d="M3 1 1.2 2.6c0 4.4 3.8 8.2 8.2 8.2L11 9 8.6 7.2 7.3 8.4C5.8 7.7 4.3 6.2 3.6 4.7L4.8 3.4z" fill="var(--accent-blue)"/></svg>
        : (555) 014 2278
      </li>
      <li>
        <svg class="icon" width="12" height="12" viewBox="0 0 12 12"><rect x="0.5" y="2" width="11" height="8" fill="var(--accent-blue)"/><path d="M0.5 2 6 6.5 11.5 2" fill="none" stroke="#fff" stroke-width="1"/></svg>
        : cm@lumavantix.com
      </li>
    </ul>
    <div class="web">
      <svg class="icon" width="14" height="14" viewBox="0 0 14 14"><circle cx="7" cy="7" r="6" fill="var(--accent-blue)"/><path d="M1 7h12M7 1c3 3 3 9 0 12M7 1c-3 3-3 9 0 12" fill="none" stroke="#fff" stroke-width="1"/></svg>
      www.lumavantix.com
    </div>
  </section>

</main>
</body>
</html>
```